Fernwicks needs product labels for deodorant line, and future soap, and lip balm line.

Fernwicks is a new startup that at this time is looking for labels for our deodorant line. There will be future work for our other products given to the winning designer. Our products are all-natural free from petrochemicals, propylene glycol, parabens, aluminum compounds, or synthetic colorants. All our products are also handmade.
We are using a standard size stick to contain the product, on the front cap the label is 2"W x 1"H, on the body front and back the size is 2" W x 2.675" H. We want the front to say "aluminum free", and "all-natural deodorant"
The back needs to include, a UPC, Our mission is to bring you effective, all-natural products using the highest quality ingredients. , Ingredients Cocoa Butter, Shea Butter, Arrowroot Powder, Sodium Bicarbonate, Olive Oil, Water.
We are launching 4 scents.
scent free
Lavander
Tea Tree
Baby Powder
We included a couple pics of product labels we like but are definitely not limited to them. also a picture of the empty container.
Updates
Project Deadline Extended
Reason: Someone completed their design but didn't post it in time and asked me to extend the dead line.
Target Market(s)
Females that are health conscience.
Industry/Entity Type
Cosmetics

```html
<!DOCTYPE html>
<html lang="en">
<head>
<meta charset="UTF-8">
<title>Fernwicks All-Natural Deodorant Labels</title>
<link href="https://fonts.googleapis.com/css2?family=Crimson+Pro:ital,wght@0,400;0,500;1,400&family=Courier+Prime:wght@700&display=swap" rel="stylesheet">
<style>
  :root {
    --bg: #eef6f5;
    --white: #ffffff;
    --ink-grey: #77777b;
    --lavender-light: #bea8da;
    --lavender-deep: #7d55a8;
    --lavender-band: #7a4c9f;
    --powder-light: #72cde2;
    --powder-deep: #2f8fc7;
    --powder-band: #1f63b2;
    --sun-light: #f8e84e;
    --sun-deep: #f0a323;
    --sun-band: #e58a20;
    --leaf-light: #8cc95a;
    --leaf-deep: #2f8a3d;
    --leaf-band: #1f6b36;
  }
  * { box-sizing: border-box; margin: 0; padding: 0; }
  html, body { width: 1200px; height: 898px; overflow: hidden; background: var(--bg); }
  .label-sheet {
    width: 1200px; height: 898px;
    display: flex; align-items: flex-start; gap: 88px;
    padding: 208px 0 0 78px;
  }
  .scent { display: flex; flex-direction: column; gap: 29px; width: 189px; }
  .lavender  { --light: var(--lavender-light); --deep: var(--lavender-deep); --band: var(--lavender-band); }
  .powder    { --light: var(--powder-light);   --deep: var(--powder-deep);   --band: var(--powder-band); }
  .unscented { --light: var(--sun-light);      --deep: var(--sun-deep);      --band: var(--sun-band); }
  .teatree   { --light: var(--leaf-light);     --deep: var(--leaf-deep);     --band: var(--leaf-band); }

  .cap-art, .wash-art, .foot-art {
    position: absolute;
    background: linear-gradient(135deg, var(--light) 0%, var(--light) 50%, var(--deep) 100%);
  }

  .cap-label { position: relative; width: 189px; height: 95px; overflow: hidden; }
  .cap-art { inset: 0; }
  .cap-motto {
    position: absolute; left: 42px; top: 26px;
    font-family: "Courier Prime", "Courier New", monospace; font-weight: 700;
    font-size: 11px; letter-spacing: 5px; line-height: 17px; color: var(--white);
  }

  .body-label { position: relative; width: 189px; height: 254px; background: var(--white); overflow: hidden; }
  .wash-art { left: 0; top: 0; width: 189px; height: 206px; }
  .brand { position: absolute; top: 16px; left: 0; width: 100%; text-align: center; }
  .brand-dot {
    display: block; width: 54px; height: 54px; margin: 0 auto 5px;
    border-radius: 50%; background: var(--white); border: 6px solid var(--ink-grey);
  }
  .brand-name {
    font-family: "Crimson Pro", Georgia, serif; font-weight: 500; font-size: 16px; line-height: 19px;
    color: var(--ink-grey); background: var(--white); padding: 0 5px;
  }
  .claim {
    position: absolute; top: 100px; left: 0; width: 100%; text-align: center;
    color: var(--white); font-family: "Crimson Pro", Georgia, serif;
  }
  .claim-natural { font-style: italic; font-size: 22px; line-height: 22px; }
  .claim-product { font-size: 24px; line-height: 25px; letter-spacing: .3px; }
  .claim-free {
    display: flex; align-items: center; justify-content: center; gap: 7px;
    font-size: 12px; line-height: 14px;
  }
  .claim-free::before, .claim-free::after { content: ""; width: 28px; height: 1px; background: var(--white); }
  .scent-band {
    position: absolute; top: 206px; left: 0; width: 100%; height: 17px; background: var(--band);
    color: var(--white); font-family: "Crimson Pro", Georgia, serif; font-size: 11px; line-height: 17px;
    letter-spacing: .3px; text-align: center; text-transform: uppercase;
  }
  .net-weight {
    position: absolute; top: 225px; left: 0; width: 100%; text-align: center;
    font-family: "Crimson Pro", Georgia, serif; font-size: 8px; line-height: 10px; color: var(--band);
  }
  .foot-art { left: 0; top: 240px; width: 100%; height: 14px; }
</style>
</head>
<body>
<main class="label-sheet">

  <section class="scent lavender">
    <div class="cap-label">
      <div class="cap-art" role="img" aria-label="Watercolour lavender sprigs on a purple wash"></div>
      <p class="cap-motto">HAND MADE<br>WITH LOVE</p>
    </div>
    <div class="body-label">
      <div class="wash-art" role="img" aria-label="Purple watercolour wash with lavender sprigs"></div>
      <div class="brand"><span class="brand-dot"></span><span class="brand-name">Fernwicks</span></div>
      <div class="claim">
        <p class="claim-natural">all - natural</p>
        <p class="claim-product">DEODORANT</p>
        <p class="claim-free">aluminum free</p>
      </div>
      <p class="scent-band">Fresh Lavender</p>
      <p class="net-weight">75g / 2.65oz</p>
      <div class="foot-art" role="img" aria-label="Lavender sprigs border"></div>
    </div>
  </section>

  <section class="scent powder">
    <div class="cap-label">
      <div class="cap-art" role="img" aria-label="Blue watercolour wildflower stems"></div>
      <p class="cap-motto">HAND MADE<br>WITH LOVE</p>
    </div>
    <div class="body-label">
      <div class="wash-art" role="img" aria-label="Blue watercolour wash with wildflower stems"></div>
      <div class="brand"><span class="brand-dot"></span><span class="brand-name">Fernwicks</span></div>
      <div class="claim">
        <p class="claim-natural">all - natural</p>
        <p class="claim-product">DEODORANT</p>
        <p class="claim-free">aluminum free</p>
      </div>
      <p class="scent-band">Powder Scent</p>
      <p class="net-weight">75g / 2.65oz</p>
      <div class="foot-art" role="img" aria-label="Blue wildflower border"></div>
    </div>
  </section>

  <section class="scent unscented">
    <div class="cap-label">
      <div class="cap-art" role="img" aria-label="Yellow and orange watercolour round blossoms"></div>
      <p class="cap-motto">HAND MADE<br>WITH LOVE</p>
    </div>
    <div class="body-label">
      <div class="wash-art" role="img" aria-label="Yellow watercolour wash with orange round blossoms"></div>
      <div class="brand"><span class="brand-dot"></span><span class="brand-name">Fernwicks</span></div>
      <div class="claim">
        <p class="claim-natural">all - natural</p>
        <p class="claim-product">DEODORANT</p>
        <p class="claim-free">aluminum free</p>
      </div>
      <p class="scent-band">Scent Free</p>
      <p class="net-weight">75g / 2.65oz</p>
      <div class="foot-art" role="img" aria-label="Orange blossom border"></div>
    </div>
  </section>

  <section class="scent teatree">
    <div class="cap-label">
      <div class="cap-art" role="img" aria-label="Green watercolour tea tree leaves"></div>
      <p class="cap-motto">HAND MADE<br>WITH LOVE</p>
    </div>
    <div class="body-label">
      <div class="wash-art" role="img" aria-label="Green watercolour wash with tea tree leaves"></div>
      <div class="brand"><span class="brand-dot"></span><span class="brand-name">Fernwicks</span></div>
      <div class="claim">
        <p class="claim-natural">all - natural</p>
        <p class="claim-product">DEODORANT</p>
        <p class="claim-free">aluminum free</p>
      </div>
      <p class="scent-band">Tea Tree</p>
      <p class="net-weight">75g / 2.65oz</p>
      <div class="foot-art" role="img" aria-label="Tea tree leaf border"></div>
    </div>
  </section>

</main>
</body>
</html>
```